Im open to ideas.. I was thinking on my business cards aswell as my logo. a place for my name. email. phone number and abn..

ive attched a file with my business logo. which i dont love the colours.. i was think a dark background with charcoal letters so something along those colour schumes but im open to ideas..

Business

BRL Constructions

```html
<!DOCTYPE html>
<html lang="en">
<head>
<meta charset="utf-8">
<title>BRL Constructions – Business Cards</title>
<link href="https://fonts.googleapis.com/css2?family=Open+Sans:wght@400;600;700;800&display=swap" rel="stylesheet">
<style>
  :root {
    --bg: #e6e7e8;
    --red: #ec1c24;
    --red-soft: #ef3a3f;
    --charcoal: #231f20;
    --white: #ffffff;
    --rule: #3a3a3a;
  }
  * { box-sizing: border-box; margin: 0; padding: 0; }
  html, body { width: 1200px; height: 1200px; overflow: hidden; }
  body {
    background: var(--bg);
    font-family: "Open Sans", Arial, sans-serif;
    position: relative;
  }

  .brand-mark {
    position: absolute;
    top: 120px;
    right: 96px;
    font-weight: 800;
    font-size: 50px;
    color: var(--charcoal);
    letter-spacing: 1px;
  }

  .card {
    position: absolute;
    box-shadow: 0 18px 40px rgba(0,0,0,0.18);
  }

  /* Front card */
  .card-front {
    left: 70px;
    top: 420px;
    width: 620px;
    height: 354px;
    background: var(--white);
    overflow: hidden;
  }
  .card-front .brand-name {
    position: absolute;
    left: 40px;
    top: 62px;
    font-weight: 800;
    font-size: 34px;
    color: var(--charcoal);
  }
  .card-front .holder {
    position: absolute;
    right: 36px;
    top: 44px;
    text-align: right;
  }
  .holder-name {
    font-weight: 700;
    font-size: 30px;
    color: var(--charcoal);
    line-height: 1;
  }
  .holder-role {
    font-weight: 700;
    font-size: 16px;
    color: var(--red);
    margin-top: 4px;
  }

  .contacts {
    position: absolute;
    left: 20px;
    right: 20px;
    top: 160px;
    height: 100px;
    display: flex;
  }
  .contact {
    flex: 1;
    display: flex;
    flex-direction: column;
    align-items: center;
    justify-content: flex-end;
    gap: 14px;
  }
  .contact + .contact { border-left: 1.5px solid var(--rule); }
  .contact-icon { width: 48px; height: 48px; }
  .contact-text {
    font-size: 13px;
    font-weight: 600;
    color: var(--charcoal);
    white-space: nowrap;
  }

  .address-band {
    position: absolute;
    left: 0; right: 0; bottom: 0;
    height: 62px;
    background: var(--red);
    color: var(--white);
    font-weight: 700;
    font-size: 17px;
    display: flex;
    align-items: center;
    justify-content: center;
  }

  /* Back card */
  .card-back {
    left: 770px;
    top: 300px;
    width: 354px;
    height: 620px;
    background: linear-gradient(160deg, var(--red) 0%, var(--red-soft) 100%);
  }
  .card-back .brand-name {
    position: absolute;
    left: 50%;
    top: 50%;
    transform: translate(-50%, -50%) rotate(-90deg);
    font-weight: 800;
    font-size: 44px;
    color: var(--white);
    white-space: nowrap;
  }
</style>
</head>
<body>

  <div class="brand-mark">BRL Constructions</div>

  <section class="card card-front" aria-label="Business card front">
    <div class="brand-name">BRL Constructions</div>

    <div class="holder">
      <div class="holder-name">DANIEL HART</div>
      <div class="holder-role">SALES MANAGER</div>
    </div>

    <div class="contacts">
      <div class="contact">
        <svg class="contact-icon" viewBox="0 0 48 48" aria-hidden="true">
          <circle cx="24" cy="24" r="24" fill="var(--red)"/>
          <rect x="13" y="16" width="22" height="16" rx="1.5" fill="var(--white)"/>
          <path d="M13 17 L24 26 L35 17" fill="none" stroke="var(--red)" stroke-width="2"/>
        </svg>
        <span class="contact-text">info@brlconstructions.com</span>
      </div>
      <div class="contact">
        <svg class="contact-icon" viewBox="0 0 48 48" aria-hidden="true">
          <circle cx="24" cy="24" r="24" fill="var(--red)"/>
          <rect x="17" y="11" width="14" height="26" rx="2.5" fill="none" stroke="var(--white)" stroke-width="2.5"/>
          <circle cx="24" cy="32" r="1.6" fill="var(--white)"/>
        </svg>
        <span class="contact-text">(555) 014-2290</span>
      </div>
      <div class="contact">
        <svg class="contact-icon" viewBox="0 0 48 48" aria-hidden="true">
          <circle cx="24" cy="24" r="24" fill="var(--red)"/>
          <g fill="none" stroke="var(--white)" stroke-width="2">
            <circle cx="24" cy="24" r="12"/>
            <ellipse cx="24" cy="24" rx="5.5" ry="12"/>
            <line x1="12" y1="24" x2="36" y2="24"/>
            <line x1="14" y1="18" x2="34" y2="18"/>
            <line x1="14" y1="30" x2="34" y2="30"/>
          </g>
        </svg>
        <span class="contact-text">www.brlconstructions.com</span>
      </div>
    </div>

    <div class="address-band">24 Alder Road Millbrook, NH 03000-0100</div>
  </section>

  <section class="card card-back" aria-label="Business card back">
    <div class="brand-name">BRL Constructions</div>
  </section>

</body>
</html>
```